Legal Information Website

We need a website that will serve as a source of information for people visiting, living, and working in the United Arab Emirates, where they can go and read about legal issues, laws, crimes, and most important find legal advice and find lawyers. The following are the pages of the website:

Find a Lawyer (Home Page)
This main feature of this page should be "Find a Lawyer"
Find a Lawyer should include the searching option by practice, by lawyer’s name, by law firm name or by location.

Ask a lawyer
This function allows the user to ask a lawyer a legal question and get an answer directly from a lawyer.

Research a legal matter
This function allows the user to do research on a certain legal topic. He/she can select from different legal topics.

Contact Us:
This page should include our contact details for the visitors in case they need any assistance. Contact us by Phone, Email, or Chat.

Once the design is approved, we will provide the rest of the website text.

Target Market(s)

General Public who seek legal advice

Industry/Entity Type

Law Firm

Font styles to use
Serif
Sans Serif

Requirements
Must have
• A tool to search for lawyer's, and then display the lawyer's picture and profile and credentials.

```html
<!DOCTYPE html>
<html lang="en">
<head>
<meta charset="utf-8">
<title>LEXPOINT – Find a Lawyer</title>
<link href="https://fonts.googleapis.com/css2?family=Roboto:wght@300;400;500;700&display=swap" rel="stylesheet">
<style>
:root{
  --brand-red:#8a0f0f;
  --nav-red:#a30d0d;
  --nav-red-dark:#7a0707;
  --heading-red:#6d0a0a;
  --ink:#1d1d1d;
  --text:#333;
  --muted:#777;
  --page:#f5f5f5;
  --dark:#1e2022;
  --dark-2:#2b2e31;
  --yellow:#f7c100;
  --yellow-dark:#f0a400;
  --accent:#e8670c;
  --line:#e2e2e2;
}
*{box-sizing:border-box;margin:0;padding:0}
html,body{width:1128px;height:1200px;overflow:hidden}
body{font-family:'Roboto',Arial,sans-serif;background:var(--page);color:var(--text);position:relative}

/* header */
.site-header{position:absolute;left:0;top:0;width:1128px;height:54px;background:linear-gradient(#fff,#f1f1f1)}
.brand{position:absolute;left:152px;top:10px;font-size:29px;font-weight:700;color:var(--brand-red);letter-spacing:.3px}
.help{position:absolute;right:152px;top:13px;display:flex;align-items:center;gap:6px;font-size:13px;color:var(--ink)}
.help strong{font-size:23px;font-weight:700;color:var(--brand-red)}

/* nav */
.main-nav{position:absolute;left:0;top:54px;width:1128px;height:43px;background:linear-gradient(var(--nav-red),var(--nav-red-dark));border-top:1px solid #c52a2a}
.main-nav ul{list-style:none;position:absolute;left:152px;top:0;height:43px;display:flex;border-left:1px solid rgba(0,0,0,.18)}
.main-nav li{height:43px;line-height:43px;padding:0 20px;font-size:15px;font-weight:500;color:#fff;border-right:1px solid rgba(0,0,0,.18);box-shadow:1px 0 0 rgba(255,255,255,.08)}
.chat-btn{position:absolute;left:808px;top:6px;width:166px;height:31px;background:linear-gradient(var(--yellow),var(--yellow-dark));display:flex;justify-content:space-between}
.chat-btn span{padding:4px 0 0 11px;font-size:8px;color:#4a2a00;line-height:9px}
.chat-btn b{display:block;font-size:15px;line-height:16px;font-weight:500;color:#6a0d0d}
.chat-btn .agent{width:36px;height:31px;background:linear-gradient(#f3d9c4,#c89a72)}

/* hero */
.hero{position:absolute;left:0;top:97px;width:1128px;height:386px;background:linear-gradient(90deg,#eef0f1 0%,#e7e9ea 45%,#d9dcdf 60%,#cfd2d5 100%)}
.hero-photo{position:absolute;left:580px;top:97px;width:420px;height:386px;background:linear-gradient(160deg,#c9ccd0,#3a3f48 55%,#23272e)}
.hero-title{position:absolute;left:152px;top:226px;font-size:46px;font-weight:700;color:var(--ink);letter-spacing:.5px}
.hero-sub{position:absolute;left:152px;top:288px;font-size:21px;font-weight:300;line-height:27px;color:var(--ink)}
.dots{position:absolute;left:153px;top:422px;display:flex;gap:3px}
.dots i{width:12px;height:12px;border-radius:50%;border:1.5px solid var(--nav-red);background:#fff}
.dots i.on{background:var(--ink);border-color:var(--ink)}

/* tabs */
.tabs{position:absolute;left:0;top:483px;width:1128px;height:64px;background:var(--dark)}
.tab{position:absolute;top:0;width:274px;height:64px;text-align:center;border-right:1px solid #111;padding-top:15px;font-size:14px;font-weight:300;color:#cfcfcf}
.tab b{display:block;font-weight:500;color:#fff;margin-top:3px}
.tab b em{font-style:normal;color:var(--yellow)}
.tab.active{background:var(--dark-2);border-bottom:3px solid var(--nav-red)}
.tab.active::after{content:"";position:absolute;left:131px;bottom:0;border:6px solid transparent;border-bottom-color:var(--nav-red)}

/* search */
.search{position:absolute;left:152px;top:547px;width:824px;height:56px;background:#e4e4e4;border:1px solid #d6d6d6;border-top:0}
.field{position:absolute;top:14px;height:27px;width:207px;background:#fff;border:1px solid #ccc;font-size:11px;color:#555;padding:7px 12px}
.search-btn{position:absolute;left:680px;top:13px;width:118px;height:28px;background:linear-gradient(var(--yellow),var(--yellow-dark));border:1px solid #d89200;font-size:15px;font-weight:500;color:#3a2600;text-align:center;line-height:27px}

/* news */
.news{position:absolute;left:152px;top:658px;width:229px;height:288px;background:#fff;border:1px solid var(--line)}
.news h3{position:absolute;left:20px;top:19px;font-size:16px;font-weight:500;color:var(--heading-red)}
.news-item{position:absolute;left:20px;width:188px;border-bottom:1px solid var(--line);padding-bottom:10px}
.news-item p{font-size:11.5px;line-height:15px;color:#222}
.news-item small{display:block;font-size:8px;color:#444;margin-top:4px}
.news-item small span{color:var(--accent)}
.see-all{position:absolute;left:20px;top:256px;width:58px;height:21px;background:linear-gradient(var(--yellow),var(--yellow-dark));border:1px solid #d89200;font-size:8.5px;font-weight:500;text-align:center;line-height:20px;color:#3a2600}

/* welcome */
.welcome{position:absolute;left:428px;top:657px;width:548px}
.welcome h1{font-size:29px;font-weight:700;color:var(--heading-red);letter-spacing:.2px}
.welcome .lead{margin-top:10px;font-size:14px;line-height:19px;color:#222;text-align:justify}
.welcome .body{margin-top:14px;font-size:11.5px;line-height:15.8px;color:var(--muted);text-align:justify}

/* promo band */
.promo-band{position:absolute;left:0;top:997px;width:1128px;height:142px;background:#fff;border-top:1px solid var(--line)}
.promo{position:absolute;top:26px;width:260px;height:91px;overflow:hidden;color:#fff}
.promo h4{position:absolute;font-size:16px;font-weight:500;line-height:17px}
.promo p{position:absolute;font-size:9px;line-height:11px}
.promo-team{left:152px;background:#222}
.promo-team .pic{position:absolute;left:100px;top:0;width:160px;height:91px;background:linear-gradient(90deg,#2a2a2a,#6b5a4c 40%,#8c7a6a)}
.promo-lang{left:434px;background:#b41414}
.promo-lang .pic{position:absolute;left:15px;top:11px;width:69px;height:69px;border-radius:50%;background:radial-gradient(circle at 40% 40%,#f2c431,#e0452f 45%,#3b9bd8 80%)}
.promo-chat{left:716px;background:linear-gradient(90deg,#5b5b5b,#9a9a9a)}
.promo-chat .pic{position:absolute;left:140px;top:0;width:120px;height:91px;background:linear-gradient(90deg,#b8b8b8,#e9d3c2 50%,#d5b59b)}
.online{position:absolute;left:21px;top:54px;width:87px;height:17px;background:var(--yellow);color:#3a1000;font-size:10px;font-weight:700;text-align:center;line-height:17px}

/* footer */
.site-footer{position:absolute;left:0;top:1139px;width:1128px;height:61px;background:#222}
.foot-links{position:absolute;left:152px;top:17px;font-size:9px;color:#bbb;line-height:15px}
.foot-links .sep{color:#666;margin:0 5px}
.social{display:inline-flex;gap:5px;margin-left:10px;vertical-align:middle}
.social i{width:7px;height:7px;border-radius:50%;background:#ddd}
.foot-brand{position:absolute;right:152px;top:19px;font-size:20px;font-weight:700;color:#8a8a8a}
</style>
</head>
<body>

<header class="site-header">
  <div class="brand">LEXPOINT</div>
  <div class="help">Get Help Now :
    <svg width="13" height="20" viewBox="0 0 13 20" aria-hidden="true"><rect x="1" y="1" width="11" height="18" rx="2" fill="none" stroke="#1d1d1d" stroke-width="2"/><circle cx="6.5" cy="16" r="1" fill="#1d1d1d"/></svg>
    <strong>800 555 0199</strong>
  </div>
</header>

<nav class="main-nav">
  <ul>
    <li>Home</li>
    <li>Ask a Lawyer</li>
    <li>Find a Lawyer</li>
    <li>Research a Legal Matter</li>
    <li>Contact Us</li>
  </ul>
  <div class="chat-btn">
    <span>CLICK HERE TO<b>CHAT LIVE</b></span>
    <div class="agent" role="img" aria-label="Support agent with headset"></div>
  </div>
</nav>

<section class="hero" role="img" aria-label="Bright modern law office interior"></section>
<div class="hero-photo" role="img" aria-label="Lawyer in a suit seated at his desk"></div>
<h2 class="hero-title">FIND A LAWYER</h2>
<p class="hero-sub">Your Number one Source for Finding<br>the Best Lawyers in the City.</p>
<div class="dots"><i></i><i class="on"></i><i></i></div>

<div class="tabs">
  <div class="tab active" style="left:152px">Have an urgent problem?<b>FIND A LAWYER</b></div>
  <div class="tab" style="left:426px">Looking for information?<b>RESEARCH LEGAL ADVICE</b></div>
  <div class="tab" style="left:700px">Didn’t find answer?<b>ASK A LAWYER &nbsp;- &nbsp;<em>FREE</em></b></div>
</div>

<form class="search">
  <div class="field" style="left:26px">Lawer’s Name</div>
  <div class="field" style="left:244px">Law Firm Name</div>
  <div class="field" style="left:462px">By Location</div>
  <div class="search-btn">SEARCH</div>
</form>

<aside class="news">
  <h3>RECENT NEWS</h3>
  <div class="news-item" style="top:60px">
    <p>Verdict in Florida 'loud music' death again raises self- defense issue</p>
    <small>The Daily Ledger <span>2 days ago</span></small>
  </div>
  <div class="news-item" style="top:127px">
    <p>Daniel Harlow on Vistaline: I'm homeless, suffering from PTSD</p>
    <small>The Coastal Tribune <span>3 days ago</span></small>
  </div>
  <div class="news-item" style="top:194px">
    <p>Halvorsen apologizes to Carter, Reed and Walsh</p>
    <small>Newswire Daily <span>2 days ago</span></small>
  </div>
  <div class="see-all">SEE ALL</div>
</aside>

<section class="welcome">
  <h1>WELCOME TO OUR WEBSITE</h1>
  <p class="lead">This is Sketchwise's version &nbsp;of Lorem Ipsum. Proin gravida nibh vel velit auctor aliquet. Aenean sollicitudin, lorem quis bibendum auctor, nisi elit consequat ipsum, nec sagittis sem nibh id elit.</p>
  <p class="body">Duis sed odio sit amet nibh vulputate cursus a sit amet mauris. Morbi accumsan ipsum velit. Nam nec tellus a odio tincidunt auctor a ornare odio. Sed non &nbsp;mauris vitae erat consequat auctor eu in elit. Class aptent taciti sociosqu ad litora torquent per conubia nostra, per inceptos himenaeos. Mauris in erat justo. Nullam ac urna eu felis dapibus condimentum sit amet a augue. Sed non neque elit. Sed ut imperdiet nisi. Proin condimentum fermentum nunc. Etiam pharetra, erat sed fermentum feugiat, velit mauris egestas quam, ut aliquam massa nisl quis neque. Suspendisse in orci enim.Duis sed odio sit amet nibh vulputate cursus a sit amet mauris. Morbi accumsan ipsum velit. Nam nec tellus a odio tincidunt auctor a ornare odio. Sed non &nbsp;mauris vitae erat consequat auctor eu in elit. Class aptent taciti sociosqu ad litora torquent per conubia nostra, per inceptos himenaeos. Mauris in erat justo. Nullam ac urna eu felis dapibus condimentum sit amet a augue.</p>
</section>

<section class="promo-band">
  <div class="promo promo-team">
    <div class="pic" role="img" aria-label="Legal team working together at a table"></div>
    <h4 style="left:12px;top:25px">MEET OUR TEAM</h4>
    <p style="left:12px;top:43px">This is Sketchwise's version of<br>Lorem Ipsum. Proin gravida</p>
  </div>
  <div class="promo promo-lang">
    <div class="pic" role="img" aria-label="Colourful speech bubbles forming a globe"></div>
    <h4 style="left:95px;top:25px">WE SPEAK</h4>
    <p style="left:95px;top:43px">English, &nbsp;| &nbsp;Spanish &nbsp;| &nbsp;Portuguese &nbsp;|<br>Russian | &nbsp;Indo-European</p>
  </div>
  <div class="promo promo-chat">
    <div class="pic" role="img" aria-label="Smiling support agent with headset"></div>
    <p style="left:21px;top:20px;font-size:11px">Click to here</p>
    <h4 style="left:21px;top:32px;font-size:17px">CHAT LIVE</h4>
    <div class="online">ONLINE NOW</div>
  </div>
</section>

<footer class="site-footer">
  <div class="foot-links">
    Home<span class="sep">|</span>Contact Us<br>
    Copyrights © 2014, All rights reserved.
    <span class="social"><i></i><i></i></span>
  </div>
  <div class="foot-brand">LEXPOINT</div>
</footer>

</body>
</html>
```